Package Design for Chew Bone Guild for Rivora

Would like a label to put on a 6x9 package.

Here is my site: chewboneguild.example

Here are the labels I like:
https://tomandhound.example/collections/chews/products/6-inch-basic-chews
https://www.rivora.example/stores/Tom+%26+Hound/page/A1D23456-7ABC-42EF-9D01-123456789ABC?ref_=xyz_qrs
https://quiet-meadowland.example/amber-paw-mini-chews-6-25-pack/
https://www.fernandkettle.example/shop/open-trail-chew-rods

```html
<!DOCTYPE html>
<html lang="en">
<head>
<meta charset="utf-8">
<title>Chew Bone Guild – Bully Sticks Label</title>
<link href="https://fonts.googleapis.com/css2?family=Montserrat:wght@400;500;600;700;800;900&display=swap" rel="stylesheet">
<style>
  :root {
    --stage: #3a3a3c;
    --label-bg: #dfe3e7;
    --tab-green: #b2c9a0;
    --lime: #8cc63f;
    --deep-green: #4f7a3a;
    --brown: #7a4a26;
    --dark-brown: #3b2414;
    --ink: #2c2e33;
    --white: #ffffff;
    --text: #3c3c3c;
  }
  * { box-sizing: border-box; margin: 0; padding: 0; }
  html, body { width: 819px; height: 1200px; overflow: hidden; }
  body {
    background: var(--stage);
    font-family: "Montserrat", sans-serif;
    position: relative;
  }
  .label {
    position: absolute;
    top: 315px;
    width: 380px;
    height: 569px;
    background: var(--label-bg);
    overflow: hidden;
    box-shadow: 0 4px 10px rgba(0,0,0,0.35);
  }
  .label--front { left: 20px; }
  .label--back { left: 419px; }

  .brand-tab {
    position: absolute;
    left: 102px; top: 0;
    width: 176px; height: 231px;
    background: var(--tab-green);
    border-radius: 0 0 88px 88px;
  }
  .brand-mark {
    position: absolute;
    left: 50%; top: 60px;
    width: 100px; height: 100px;
    margin-left: -50px;
    background: var(--white);
    border-radius: 50%;
  }
  .brand-name {
    position: absolute;
    left: 0; right: 0; top: 176px;
    text-align: center;
    font-weight: 800;
    font-size: 15px;
    color: var(--brown);
  }

  /* front */
  .tagline {
    position: absolute;
    left: 0; right: 0; top: 250px;
    text-align: center;
    font-weight: 500;
    font-size: 13px;
    letter-spacing: 4.2px;
    color: var(--ink);
  }
  .title-main {
    position: absolute;
    left: 30px; top: 262px;
    font-weight: 900;
    font-size: 89px;
    line-height: 1;
    letter-spacing: -1px;
    color: var(--brown);
  }
  .title-sub {
    position: absolute;
    left: 58px; top: 341px;
    font-weight: 900;
    font-size: 42px;
    line-height: 1;
    letter-spacing: -1px;
    color: var(--brown);
  }
  .title-badge {
    position: absolute;
    left: 221px; top: 348px;
    width: 101px; height: 29px;
    background: var(--lime);
    color: var(--brown);
    font-weight: 500;
    font-size: 11px;
    line-height: 12px;
    padding: 3px 0 0 7px;
  }
  .benefits {
    position: absolute;
    left: 22px; top: 401px;
    width: 168px;
    list-style: none;
  }
  .benefits li {
    height: 21px;
    line-height: 21px;
    padding-left: 8px;
    font-weight: 700;
    font-size: 11.5px;
    color: var(--white);
    background: var(--ink);
  }
  .benefits li:nth-child(even) { background: var(--lime); }
  .benefits li::before { content: "• "; }

  .sticks-art {
    position: absolute;
    left: 22px; top: 486px;
    width: 150px; height: 44px;
    background: linear-gradient(160deg, #b8642a, #8a4a1e 60%, #c98a4a);
    border-radius: 6px;
  }
  .size-note {
    position: absolute;
    left: 42px; top: 526px;
    display: flex; align-items: center; gap: 3px;
    color: var(--ink);
    font-weight: 800;
  }
  .size-note__num { font-size: 25px; line-height: 1; }
  .size-note__txt { font-size: 10.5px; line-height: 10px; }

  .swoosh { position: absolute; left: 0; top: 0; width: 380px; height: 569px; }

  .dogs-photo {
    position: absolute;
    left: 194px; top: 382px;
    width: 172px; height: 182px;
    background: linear-gradient(90deg, #2a2624 0%, #4a3e38 48%, #cdbb9e 52%, #e4d7bf 100%);
    border-radius: 40px 40px 4px 4px;
  }

  /* back */
  .story {
    position: absolute;
    left: 24px; right: 24px; top: 254px;
    text-align: center;
    font-size: 6.3px;
    line-height: 8.4px;
    color: var(--brown);
  }
  .story p + p { margin-top: 6px; }
  .story strong { font-weight: 700; }

  .perk {
    position: absolute;
    top: 334px;
    height: 38px;
    background: var(--lime);
    color: var(--brown);
    font-weight: 600;
    font-size: 7.6px;
    line-height: 9px;
    text-align: center;
    padding-top: 14px;
  }
  .perk--delivery { left: 21px; width: 102px; }
  .perk--service { left: 132px; width: 115px; }
  .perk--range { left: 255px; width: 102px; }
  .perk__icon {
    position: absolute;
    left: 50%; top: -14px;
    width: 24px; height: 24px;
    margin-left: -12px;
    border-radius: 50%;
    background: var(--brown);
  }
  .range-title {
    position: absolute;
    left: 0; right: 0; top: 384px;
    text-align: center;
    font-weight: 600;
    font-size: 10.5px;
    color: var(--ink);
  }
  .range-list {
    position: absolute;
    left: 0; right: 0; top: 402px;
    text-align: center;
    font-weight: 700;
    font-size: 7.4px;
    line-height: 9.4px;
    color: var(--brown);
  }
  .barcode-box {
    position: absolute;
    left: 23px; top: 470px;
    width: 127px; height: 76px;
    background: var(--white);
    border: 3px solid #4a4a4a;
    font-weight: 600;
    font-size: 10px;
    color: var(--ink);
    display: flex; align-items: center; justify-content: center;
  }
  .cattle-art {
    position: absolute;
    left: 224px; top: 462px;
    width: 138px; height: 98px;
    background: radial-gradient(ellipse at 55% 45%, #6f9a3a 0%, #86b440 55%, rgba(140,198,63,0) 75%);
  }
</style>
</head>
<body>

<section class="label label--front" aria-label="Front label">
  <svg class="swoosh" viewBox="0 0 380 569" aria-hidden="true">
    <path d="M92,569 C190,515 290,462 380,420 L380,436 C300,470 210,520 120,569 Z" fill="var(--deep-green)"/>
    <path d="M120,569 C210,520 300,472 380,436 L380,569 Z" fill="var(--lime)"/>
  </svg>

  <div class="brand-tab">
    <div class="brand-mark"></div>
    <div class="brand-name">Chew Bone Guild</div>
  </div>

  <p class="tagline">NATURALLY ODOR FREE</p>
  <h1 class="title-main">BULLY</h1>
  <h2 class="title-sub">STICKS</h2>
  <div class="title-badge">PREMIUM<br>DOG CHEWS</div>

  <ul class="benefits">
    <li>PREMIUM GRADE</li>
    <li>FOR DENTAL HEALTH</li>
    <li>GRASS-FED BEEF</li>
    <li>100% DIGESTIBLE</li>
  </ul>

  <div class="sticks-art" role="img" aria-label="Illustration of crossed bully sticks"></div>
  <div class="size-note">
    <span class="size-note__num">6”</span>
    <span class="size-note__txt">BULLY<br>STICKS</span>
  </div>

  <div class="dogs-photo" role="img" aria-label="Photo of a black dog with a red bandana and a cream dog with a black bandana sitting side by side"></div>
</section>

<section class="label label--back" aria-label="Back label">
  <svg class="swoosh" viewBox="0 0 380 569" aria-hidden="true">
    <path d="M92,569 C190,520 290,455 380,420 L380,436 C300,468 210,525 120,569 Z" fill="var(--deep-green)"/>
    <path d="M120,569 C210,525 300,470 380,436 L380,569 Z" fill="var(--lime)"/>
  </svg>

  <div class="brand-tab">
    <div class="brand-mark"></div>
    <div class="brand-name">Chew Bone Guild</div>
  </div>

  <div class="story">
    <p><strong>We love our dogs.</strong> They’re our adventure buddies, best friends and occasional alarm clocks. For all they do for us, they deserve the best. When our founders were unable to find <strong>high quality, all natural chews and treats</strong> to meet their standards for their own pups, they became inspired.</p>
    <p>They set out on a passionate, worldwide journey to find innovative, nutrition-packed and most importantly, delicious chews and treats. Today, we continue their mission to the tail wagging satisfaction of dogs everywhere. Thank you for welcoming <strong>Chew Bone Guild</strong> into your family!</p>
  </div>

  <div class="perk perk--delivery"><span class="perk__icon" role="img" aria-label="Paw icon"></span>Fast &amp; Reliable<br>Delivery</div>
  <div class="perk perk--service"><span class="perk__icon" role="img" aria-label="Paw icon"></span>Consistent Customer<br>&amp; Pet Satisfaction</div>
  <div class="perk perk--range"><span class="perk__icon" role="img" aria-label="Paw icon"></span>Vast Products<br>Selection</div>

  <p class="range-title">TRY ALL OF OUR ALL NATURAL DOG TREATS AND CHEWS</p>
  <p class="range-list">• BULLY STICKS • BONES • EARS • JERKY • ANTLERS<br>TENDONS • TRACHEAS AND MORE</p>

  <div class="barcode-box">BAR CODE</div>
  <div class="cattle-art" role="img" aria-label="Green sketch of a grazing steer"></div>
</section>

</body>
</html>
```